Book Cover: Using Programming to "Hack" Wall Street

We need a book cover design for a soon-to-be-published book focused on how technology will disrupt stock market trading ("Wall Street"). The book will be called "Scripting Harbor Av." or "Scripting Harbor Avenue"
Specifically, the book discusses how the use of programming code to "web scrape"/"data harvest" data on publicly traded companies websites [example: pellmart.com] can be used to track their business sales in real time. I'm hoping for an image that convey's A) a tech-savvy/programming, B) stock market trading/prices/Wall Street, and C) a "clean" feel (doesn't feel "busy"). Open to any/all ideas (i will know what I like), and with a preference (but not requirement) for a somewhat-dark green or blue color.
If you'd like a bit more background, www.crestvaleinsight.com is a "work in progress" website that discusses some of the ideas that will be embodied in the book (please don't use it for any design ideas).
Note: book size will likely be 8.5x11 or 6x9
Also -- separate to the book -- I will likely sell case studies [pdf downloads]; would be great to have a logo that pays homage to the book cover design [and vice versa]
Target Market(s)
Investment Professionals, Wall Street Traders, Stock Market Investors, Programmers, Retail Investors
Industry/Entity Type
Investment

```html
<!DOCTYPE html>
<html lang="en">
<head>
<meta charset="utf-8">
<title>Scripting Harbor Av. — Book Cover</title>
<link rel="stylesheet" href="https://fonts.googleapis.com/css2?family=Doto:wght@700;900&family=VT323&display=swap">
<style>
  :root {
    --field-deep: #1f4a22;
    --field-mid: #2f6a33;
    --field-light: #3d7d3f;
    --grain-dark: rgba(12, 40, 14, 0.45);
    --grain-light: rgba(150, 210, 140, 0.18);
    --title-fill: #b9dcb4;
    --title-edge: #dff0da;
    --tag-bg: #1b2b1c;
    --tag-text: #f2f5f0;
    --band-bg: rgba(20, 32, 22, 0.9);
    --band-text: #f4f7f2;
  }
  html, body {
    margin: 0;
    padding: 0;
    width: 857px;
    height: 1200px;
    overflow: hidden;
    background: var(--field-deep);
  }
  .cover {
    position: relative;
    width: 857px;
    height: 1200px;
    overflow: hidden;
  }
  .code-field {
    position: absolute;
    inset: 0;
    background:
      repeating-linear-gradient(0deg, var(--grain-dark) 0 1px, transparent 1px 3px, var(--grain-light) 3px 4px, transparent 4px 6px),
      repeating-linear-gradient(90deg, transparent 0 2px, var(--grain-dark) 2px 3px, transparent 3px 5px, var(--grain-light) 5px 6px, transparent 6px 9px),
      linear-gradient(180deg, var(--field-mid) 0%, var(--field-light) 45%, var(--field-mid) 100%);
  }
  .title {
    position: absolute;
    top: 70px;
    left: 0;
    width: 100%;
    margin: 0;
    text-align: center;
    font-family: "Doto", monospace;
    font-weight: 900;
    font-size: 128px;
    line-height: 150px;
    letter-spacing: 2px;
    color: var(--title-fill);
    text-shadow: 0 0 2px var(--title-edge);
    text-transform: uppercase;
  }
  .title span { display: block; }
  .tag {
    position: absolute;
    font-family: "VT323", monospace;
    font-size: 40px;
    line-height: 1;
    letter-spacing: 3px;
    color: var(--tag-text);
    background: var(--tag-bg);
    padding: 4px 12px 2px;
  }
  .tag-profits { left: 605px; top: 472px; }
  .tag-income  { left: 130px; top: 574px; }
  .tag-costs   { left: 565px; top: 806px; }
  .tag-sales   { left: 100px; top: 916px; }
  .tag-revenue { left: 588px; top: 1062px; }
  .tag-stores  { left: 230px; top: 1142px; }
  .subtitle-band {
    position: absolute;
    left: 0;
    top: 632px;
    width: 100%;
    padding: 8px 0;
    background: var(--band-bg);
    text-align: center;
  }
  .subtitle {
    margin: 0;
    font-family: "VT323", monospace;
    font-size: 43px;
    line-height: 50px;
    letter-spacing: 1px;
    color: var(--band-text);
  }
</style>
</head>
<body>
  <main class="cover">
    <div class="code-field" role="img" aria-label="Dense field of tiny green programming characters covering the background"></div>

    <h1 class="title">
      <span>Scripting</span>
      <span>Harbor Av.</span>
    </h1>

    <div class="tag tag-profits">PROFITS</div>
    <div class="tag tag-income">INCOME</div>

    <div class="subtitle-band">
      <p class="subtitle">A Guide for Traders and Hedge Fund Analysts<br>Using Programming Code to Track<br>Companies Financial Results in Real Time</p>
    </div>

    <div class="tag tag-costs">COSTS</div>
    <div class="tag tag-sales">SALES</div>
    <div class="tag tag-revenue">REVENUE</div>
    <div class="tag tag-stores">STORES</div>
  </main>
</body>
</html>
```